Business Card Design Project- Removalist

I would like to surprise my husband to be with a different type of wedding present. His brother (who he owned a removalist business with) suddenly passed away from cancer recently and he has changed his business name to 'RTB' (which stands for Raising Tom Bright; but the full name doesn't need to be on the business card as it is more of a personal business name). To celebrate the new business I would like to get him some business cards made.
I would like the business name to be listed as 'RTB' and somewhere on the card I would like 'Sydney wide removals and relocation services'. I would like it to be obvious from the front of the card that it is a removalist business card. If a truck or some other feature that makes it look like a removalist business card could added it would be appreciated.
I don't mind what colours are used, but I would like the colour blue to feature somewhere in the design. It can be bright and fun, which is how Tom was.
I will also need the company's email address and phone number listed
The email address is: rtbremovals@quillpost.example
The contact number is: 0417 282 934
I don't need a contact name listed on the card, but perhaps 'Owned and operated by the Pendleworth family' could be added near the contact details in small font.
Thank you very much for considering this project!
Kind regards,
Fiona
Updates
Could you please change the mobile contact number to 0417 282 934. This is the only contact phone number required on the card now.
Thank you!

```html
<!DOCTYPE html>
<html lang="en">
<head>
<meta charset="utf-8">
<title>RTB – Sydney wide removals and relocation services</title>
<link rel="stylesheet" href="https://fonts.googleapis.com/css2?family=Arimo:wght@400;700&display=swap">
<style>
  :root {
    --brand-blue: #386596;
    --frame-blue: #3a6594;
    --truck-tint: #dbe5f0;
    --paper: #ffffff;
  }
  html, body {
    margin: 0;
    padding: 0;
    width: 1200px;
    height: 671px;
    overflow: hidden;
    background: var(--paper);
  }
  .business-card {
    position: relative;
    width: 1200px;
    height: 671px;
    box-sizing: border-box;
    border: 10px solid var(--frame-blue);
    background: var(--paper);
    font-family: "Arimo", Arial, sans-serif;
    color: var(--brand-blue);
  }
  .brand-name {
    position: absolute;
    left: 183px;
    top: 128px;
    margin: 0;
    font-size: 156px;
    font-weight: 700;
    line-height: 1;
    letter-spacing: 14px;
  }
  .truck-artwork {
    position: absolute;
    left: 725px;
    top: 108px;
    width: 340px;
    height: 216px;
    background: linear-gradient(135deg, var(--truck-tint), #eef3f9);
    border-radius: 6px;
  }
  .tagline {
    position: absolute;
    left: 102px;
    top: 290px;
    margin: 0;
    font-size: 24px;
    font-weight: 700;
    letter-spacing: 0.6px;
  }
  .ground-line {
    position: absolute;
    left: 50px;
    top: 320px;
  }
  .contact-row {
    position: absolute;
    left: 64px;
    display: flex;
    align-items: center;
    gap: 14px;
    font-size: 46px;
    font-weight: 400;
  }
  .contact-row.phone { top: 404px; }
  .contact-row.email { top: 493px; }
  .ownership-note {
    position: absolute;
    left: 64px;
    top: 564px;
    margin: 0;
    font-size: 22px;
    letter-spacing: 0.3px;
  }
</style>
</head>
<body>
  <main class="business-card">
    <h1 class="brand-name">RTB</h1>
    <div class="truck-artwork" role="img" aria-label="Hand-sketched removal truck outline in blue"></div>
    <p class="tagline">Sydney wide removals and relocation services</p>
    <svg class="ground-line" width="1080" height="10" viewBox="0 0 1080 10" aria-hidden="true">
      <path d="M0 6 Q540 2 1075 4 L1075 6 Q540 6 0 7 Z" fill="var(--brand-blue)"/>
    </svg>

    <div class="contact-row phone">
      <svg width="72" height="72" viewBox="0 0 72 72" aria-hidden="true">
        <circle cx="36" cy="36" r="33" fill="none" stroke="var(--brand-blue)" stroke-width="3"/>
        <path d="M25 19 l7 -3 l5 10 l-5 4 q3 9 10 14 l4 -4 l9 6 l-3 7 q-4 3 -10 0 q-15 -9 -20 -25 q-1 -6 3 -9 Z"
              fill="none" stroke="var(--brand-blue)" stroke-width="3" stroke-linejoin="round"/>
      </svg>
      <span class="contact-value">0417 282 934</span>
    </div>

    <div class="contact-row email">
      <svg width="78" height="52" viewBox="0 0 78 52" aria-hidden="true">
        <rect x="2" y="2" width="74" height="48" rx="3" fill="none" stroke="var(--brand-blue)" stroke-width="3"/>
        <path d="M5 5 L39 32 L73 5 M5 47 L30 25 M73 47 L48 25" fill="none" stroke="var(--brand-blue)" stroke-width="3"/>
      </svg>
      <span class="contact-value">rtbremovals@quillpost.example</span>
    </div>

    <p class="ownership-note">Owned and operated by the Pendleworth family</p>
  </main>
</body>
</html>
```